New Invitation Design Project

We are looking for someone to design our e-vite, save the date and wine labels for our upcoming event on June 26th. Our event is an open house for our current clients and business colleagues to show our appreciation for them. We want to incorporate our new logo. We would like a professional but fun invitation with multiple versions in different manners of the design we choose.

Industry/Entity Type

House

```html
<!DOCTYPE html>
<html lang="en">
<head>
<meta charset="utf-8">
<title>HRM Open House Invitation</title>
<link rel="stylesheet" href="https://fonts.googleapis.com/css2?family=Ubuntu:wght@500;700&display=swap">
<style>
  :root {
    --page-bg: #e9e9ea;
    --blue-light: #6a88d6;
    --blue-deep: #4d68bf;
    --green: #8cc63f;
    --green-dark: #6fa32a;
    --charcoal: #4a4a4c;
    --charcoal-dark: #3b3b3d;
    --white: #ffffff;
    --ink: #3a3a3c;
  }
  * { box-sizing: border-box; margin: 0; padding: 0; }
  html, body { width: 1200px; height: 849px; overflow: hidden; }
  body {
    background: var(--page-bg);
    font-family: "Ubuntu", sans-serif;
    font-weight: 700;
    position: relative;
  }
  .invitation {
    position: absolute;
    left: 300px; top: 24px;
    width: 600px; height: 800px;
    background: radial-gradient(ellipse at 50% 40%, var(--blue-light) 0%, var(--blue-deep) 100%);
    box-shadow: 0 4px 18px rgba(0,0,0,.18);
    overflow: hidden;
  }
  .header-band {
    position: absolute; left: 0; top: 98px; width: 100%; height: 54px;
    background: var(--charcoal);
  }
  .brand-plate {
    position: absolute; left: 150px; top: 72px; width: 300px; height: 108px;
    background: var(--white);
    border: 6px solid var(--green);
    border-radius: 16px;
    display: flex; flex-direction: column; align-items: center; justify-content: center;
    color: var(--charcoal);
  }
  .brand-initials { font-size: 46px; line-height: 1; letter-spacing: 1px; }
  .brand-name { font-size: 20px; line-height: 1.3; margin-top: 4px; }
  .intro {
    position: absolute; top: 222px; width: 100%;
    text-align: center; color: var(--white); font-size: 22px;
  }
  .ribbon {
    position: absolute; left: 90px; top: 258px; width: 420px; height: 72px;
  }
  .ribbon-title {
    position: absolute; left: 0; top: 270px; width: 100%;
    text-align: center; color: var(--white); font-size: 27px;
  }
  .highlights {
    position: absolute; top: 345px; width: 100%;
    text-align: center; color: var(--white); list-style: none;
    font-size: 17px; line-height: 29px;
  }
  .highlights .callout { font-size: 22px; margin-top: 5px; }
  .detail-band {
    position: absolute; left: 0; width: 100%; height: 60px;
    background: var(--green);
    color: var(--ink);
    display: flex; align-items: center;
  }
  .detail-band .icon { position: absolute; left: 30px; width: 32px; height: 32px; }
  .detail-band .detail-text {
    width: 100%; text-align: center; font-size: 18px; line-height: 23px; padding-left: 40px;
  }
  .band-date { top: 472px; }
  .band-place { top: 560px; }
  .band-firm { top: 650px; }
  .rsvp-band {
    position: absolute; left: 0; top: 734px; width: 100%; height: 52px;
    background: var(--charcoal);
    color: var(--white); font-size: 17px; font-weight: 500;
    display: flex; align-items: center; justify-content: center;
  }
</style>
</head>
<body>
  <main class="invitation">
    <div class="header-band"></div>

    <div class="brand-plate">
      <span class="brand-initials">HR&amp;M</span>
      <span class="brand-name">Hale Ridgeway Moss</span>
    </div>

    <p class="intro">You're Invited to the</p>

    <svg class="ribbon" viewBox="0 0 420 72" aria-hidden="true">
      <polygon points="0,22 40,18 40,62 0,66 14,44" fill="var(--green-dark)"/>
      <polygon points="420,22 380,18 380,62 420,66 406,44" fill="var(--green-dark)"/>
      <path d="M30,10 Q210,-4 390,10 L390,56 Q210,42 30,56 Z" fill="var(--green)"/>
    </svg>
    <p class="ribbon-title">HRM Open House</p>

    <ul class="highlights">
      <li>Meet our Newest</li>
      <li>Staff Members and Attorneys</li>
      <li>Network with Our Fabulous Guests</li>
      <li class="callout">Have a Drink on Us!</li>
    </ul>

    <section class="detail-band band-date">
      <svg class="icon" viewBox="0 0 32 32" aria-hidden="true">
        <rect x="3" y="6" width="26" height="23" rx="2" fill="none" stroke="var(--white)" stroke-width="2.5"/>
        <line x1="3" y1="12" x2="29" y2="12" stroke="var(--white)" stroke-width="2.5"/>
        <line x1="10" y1="3" x2="10" y2="9" stroke="var(--white)" stroke-width="2.5"/>
        <line x1="22" y1="3" x2="22" y2="9" stroke="var(--white)" stroke-width="2.5"/>
        <g fill="var(--white)">
          <rect x="7" y="16" width="4" height="3"/><rect x="14" y="16" width="4" height="3"/><rect x="21" y="16" width="4" height="3"/>
          <rect x="7" y="22" width="4" height="3"/><rect x="14" y="22" width="4" height="3"/><rect x="21" y="22" width="4" height="3"/>
        </g>
      </svg>
      <p class="detail-text">Thursday, June 26, 2014 &nbsp;- &nbsp;3:00pm - 7:00pm<br>Drop by any time!</p>
    </section>

    <section class="detail-band band-place">
      <svg class="icon" viewBox="0 0 32 32" aria-hidden="true">
        <path d="M16,2 C9,2 5,7 5,12.5 C5,20 16,30 16,30 C16,30 27,20 27,12.5 C27,7 23,2 16,2 Z" fill="var(--white)"/>
        <circle cx="16" cy="12.5" r="4.5" fill="var(--green)"/>
      </svg>
      <p class="detail-text">2450 Linden Park Drive, &nbsp;Suite 210,<br>Maple Grove, &nbsp;IL 60190</p>
    </section>

    <section class="detail-band band-firm">
      <svg class="icon" viewBox="0 0 32 32" aria-hidden="true">
        <g fill="var(--white)">
          <circle cx="7" cy="11" r="3.5"/><rect x="2" y="16" width="10" height="10" rx="2"/>
          <circle cx="25" cy="11" r="3.5"/><rect x="20" y="16" width="10" height="10" rx="2"/>
          <circle cx="16" cy="8" r="4"/><rect x="10" y="14" width="12" height="14" rx="2"/>
        </g>
      </svg>
      <p class="detail-text">HR&amp;M - Hale, Ridgeway &amp; Moss - Attorneys at Law<br>555-014-2290 &nbsp;&nbsp;www.hrmlegal-example.com</p>
    </section>

    <footer class="rsvp-band">RSVP to jcarter@hrmlegal-example.com or (555) 014-2290</footer>
  </main>
</body>
</html>
```